business card design for a small scale specialty cut flower farm

We need a business card design for Hollowmere Bloom Farm based in Langley, BC, Canada. We produce specialty, high-end cut flowers and sell locally to florists, local shops and markets and the end user through bouquet subscriptions. The final business card design should be memorable and have a timeless or vintage feel. We would prefer a square shape.
Updates

Target Market(s)

florists, shops and seasonal markets, local flower lovers

Industry/Entity Type

Floral

Contact Information for Business Card

Tamsin Ellery Voss, Grower
Langley, BC, Canada
website: hollowmerebloomfarm.example
instagram: @hollowmerebloomfarm
Tel: 555.317.4290
facebook: www.facebook.example/hollowmereblooms/

Font styles to use
Serif
Decorative
Script

Requirements
Must have
• soft black background colour on front side, the included logo and catch phrase: Fresh Local Seasonal
Nice to have
• phone number and website address on front of card, included photo 6539 incorporated onto the back, possibly photo 6609 as well.

```html
<!DOCTYPE html>
<html lang="en">
<head>
<meta charset="utf-8">
<title>Hollowmere Bloom Farm – Business Card</title>
<link rel="stylesheet" href="https://fonts.googleapis.com/css2?family=Tinos:wght@400;700&family=Lato:wght@300;400&display=swap">
<style>
  :root {
    --page: #ffffff;
    --card-bg: #232322;
    --card-bg-edge: #1a1a19;
    --frame: #8fbf83;
    --ink: #f4f1ea;
    --ink-soft: #e2ded6;
    --ink-muted: #cfcbc2;
    --petal: #f3c9cf;
    --leaf: #8cc08a;
    --bloom-tint: rgba(243,201,207,0.45);
  }
  html, body {
    margin: 0;
    padding: 0;
    width: 1200px;
    height: 1000px;
    overflow: hidden;
    background: var(--page);
  }
  .card {
    position: absolute;
    left: 200px;
    top: 100px;
    width: 800px;
    height: 800px;
    box-sizing: border-box;
    border: 4px solid var(--frame);
    background: radial-gradient(ellipse at center, var(--card-bg) 55%, var(--card-bg-edge) 100%);
    overflow: hidden;
    font-family: "Lato", Arial, sans-serif;
    text-align: center;
  }
  .card::after {
    content: "";
    position: absolute;
    inset: 6px;
    border: 1px solid var(--frame);
    opacity: 0.6;
    pointer-events: none;
  }
  .floral-pattern {
    position: absolute;
    inset: 0;
    background:
      radial-gradient(circle at 10% 8%, rgba(243,201,207,0.14) 0, transparent 10%),
      radial-gradient(circle at 90% 10%, rgba(214,196,226,0.14) 0, transparent 10%),
      radial-gradient(circle at 92% 88%, rgba(243,201,207,0.14) 0, transparent 10%),
      radial-gradient(circle at 8% 90%, rgba(214,196,226,0.14) 0, transparent 10%);
  }
  .brand-dot {
    position: absolute;
    left: 356px;
    top: 66px;
    width: 80px;
    height: 80px;
    border-radius: 50%;
    background: var(--petal);
  }
  .brand-name {
    position: absolute;
    left: 0;
    right: 0;
    top: 176px;
    margin: 0;
    font-weight: 300;
    font-size: 34px;
    line-height: 44px;
    letter-spacing: 6px;
    text-transform: uppercase;
    color: var(--ink);
  }
  .catchphrase {
    position: absolute;
    left: 0;
    right: 0;
    top: 282px;
    margin: 0;
    font-family: "Tinos", "Times New Roman", serif;
    font-weight: 400;
    font-size: 20px;
    line-height: 24px;
    letter-spacing: 4px;
    text-transform: uppercase;
    color: var(--petal);
  }
  .vine-band {
    position: absolute;
    left: 150px;
    top: 336px;
    width: 492px;
    height: 54px;
    background:
      radial-gradient(ellipse 200px 14px at 50% 50%, rgba(140,192,138,0.55), transparent 75%),
      radial-gradient(ellipse 26px 20px at 8% 50%, var(--bloom-tint), transparent 75%),
      radial-gradient(ellipse 26px 20px at 92% 50%, var(--bloom-tint), transparent 75%);
  }
  .contact {
    position: absolute;
    left: 0;
    right: 0;
    top: 418px;
  }
  .contact-name {
    margin: 0;
    font-family: "Tinos", "Times New Roman", serif;
    font-weight: 700;
    font-size: 42px;
    line-height: 50px;
    color: var(--ink);
  }
  .contact-role {
    margin: 2px 0 0;
    font-weight: 400;
    font-size: 34px;
    line-height: 42px;
    color: var(--ink);
  }
  .contact-phone {
    margin: 8px 0 0;
    font-weight: 300;
    font-size: 40px;
    line-height: 48px;
    letter-spacing: 1px;
    color: var(--ink-muted);
  }
  .contact-web {
    margin: 2px 0 0;
    font-size: 26px;
    line-height: 34px;
    letter-spacing: 0.5px;
    color: var(--frame);
  }
  .social {
    position: absolute;
    left: 50%;
    top: 640px;
    transform: translateX(-50%);
    margin: 0;
    padding: 0;
    list-style: none;
    text-align: left;
  }
  .social-item {
    display: flex;
    align-items: center;
    gap: 8px;
    height: 38px;
    font-size: 20px;
    color: var(--ink-soft);
  }
  .social-mark {
    width: 22px;
    height: 22px;
    border-radius: 3px;
    background: var(--ink-soft);
  }
</style>
</head>
<body>
  <section class="card">
    <div class="floral-pattern" role="img" aria-label="Faint watercolour wildflowers in pale pink and lilac at the corners"></div>

    <div class="brand-dot"></div>
    <p class="brand-name">Hollowmere<br>Bloom Farm</p>
    <p class="catchphrase">Fresh · Local · Seasonal</p>

    <div class="vine-band" role="img" aria-label="Trailing vine of green leaves with small pink buds"></div>

    <div class="contact">
      <h1 class="contact-name">Tamsin Ellery Voss</h1>
      <p class="contact-role">Grower</p>
      <p class="contact-phone">(555) 317-4290</p>
      <p class="contact-web">hollowmerebloomfarm.example</p>
    </div>

    <ul class="social">
      <li class="social-item"><span class="social-mark"></span>hollowmerebloomfarm</li>
      <li class="social-item"><span class="social-mark"></span>hollowmereblooms</li>
    </ul>
  </section>
</body>
</html>
```